Business Card Ayurvedic Massage

I'm starting with my ayurvedic massage business and need a business card design. The design should be inline with my brand/logo as well as with the design of my website (www.lumo-thara.ch).
Front: logo and text "Ayurvedische Massagen"
back: name and adress (see details https://www.lumo-thara.ch/kontakt.html)

```html
<!DOCTYPE html>
<html lang="de">
<head>
<meta charset="utf-8">
<title>lumo-thara – Visitenkarte</title>
<link rel="stylesheet" href="https://fonts.googleapis.com/css2?family=Noto+Sans:wght@400;600;700&display=swap">
<style>
  :root {
    --stage: #a0a0a0;
    --label: #111111;
    --card-front: #ffffff;
    --card-back: #0b0b0b;
    --gold: #d9a21e;
    --gold-bright: #f5c242;
    --maroon: #7a1426;
    --white: #ffffff;
  }
  html, body {
    margin: 0;
    padding: 0;
    width: 1200px;
    height: 1200px;
    overflow: hidden;
    background: var(--stage);
    font-family: "Noto Sans", sans-serif;
  }
  .canvas {
    position: relative;
    width: 1200px;
    height: 1200px;
  }
  .side-label {
    position: absolute;
    left: 0;
    width: 1200px;
    text-align: center;
    margin: 0;
    font-weight: 700;
    font-size: 56px;
    line-height: 1;
    color: var(--label);
  }
  .side-label--front { top: -4px; }
  .side-label--back { top: 608px; }

  .card {
    position: absolute;
    left: 150px;
    width: 900px;
  }
  .card--front {
    top: 47px;
    height: 540px;
    background: var(--card-front);
  }
  .card--back {
    top: 660px;
    height: 540px;
    background: var(--card-back);
  }

  .elephant {
    position: absolute;
    border-radius: 30px 30px 12px 12px;
    background: linear-gradient(180deg, #e0a82a 0%, #b8861c 35%, #7a1426 70%, #c9931f 100%);
  }
  .card--front .elephant--left { left: 40px; top: 65px; width: 218px; height: 304px; }
  .card--front .elephant--right { left: 642px; top: 65px; width: 218px; height: 304px; }
  .card--back .elephant { opacity: 0.85; }
  .card--back .elephant--left { left: 31px; top: 212px; width: 171px; height: 150px; border-radius: 0 40px 30px 0; }
  .card--back .elephant--right { left: 698px; top: 212px; width: 172px; height: 150px; border-radius: 40px 0 0 30px; }

  .brand-name {
    position: absolute;
    left: 0;
    width: 900px;
    top: 205px;
    margin: 0;
    text-align: center;
    font-weight: 700;
    font-size: 62px;
    line-height: 1;
    color: var(--gold);
  }
  .tagline {
    position: absolute;
    left: 0;
    width: 900px;
    top: 402px;
    margin: 0;
    text-align: center;
    font-weight: 600;
    font-size: 57px;
    line-height: 1;
    color: var(--gold);
    text-shadow: 1px 1px 0 var(--maroon), -1px -1px 0 var(--maroon), 1px -1px 0 var(--maroon), -1px 1px 0 var(--maroon), 2px 3px 3px rgba(122,20,38,.45);
  }

  .address {
    position: absolute;
    left: 0;
    width: 900px;
    top: 100px;
    margin: 0;
    text-align: center;
    font-style: normal;
    font-weight: 700;
    font-size: 38px;
    line-height: 48px;
    color: var(--gold-bright);
  }
  .phone {
    position: absolute;
    left: 0;
    width: 900px;
    top: 262px;
    display: flex;
    justify-content: center;
    align-items: flex-end;
    gap: 4px;
    font-weight: 700;
    font-size: 32px;
    line-height: 1;
    color: var(--white);
  }
  .phone svg { width: 38px; height: 50px; }
  .email {
    position: absolute;
    left: 0;
    width: 900px;
    top: 370px;
    margin: 0;
    text-align: center;
    font-weight: 700;
    font-size: 38px;
    line-height: 1;
    color: var(--gold-bright);
  }
  .website {
    position: absolute;
    left: 0;
    width: 900px;
    top: 472px;
    margin: 0;
    text-align: center;
    font-weight: 700;
    font-size: 30px;
    line-height: 1;
    color: var(--white);
  }
</style>
</head>
<body>
<main class="canvas">
  <h2 class="side-label side-label--front">FRONT</h2>
  <section class="card card--front">
    <div class="elephant elephant--left" role="img" aria-label="Geschmückter indischer Elefant mit Schirm, nach rechts gewandt"></div>
    <h1 class="brand-name">lumo-thara</h1>
    <div class="elephant elephant--right" role="img" aria-label="Geschmückter indischer Elefant mit Schirm, nach links gewandt"></div>
    <p class="tagline">Ayurvedische Massagen</p>
  </section>

  <h2 class="side-label side-label--back">BACK</h2>
  <section class="card card--back">
    <address class="address">Mira Kessler, lumo-thara, Lindenweg 14,<br>8853 Lachen</address>
    <div class="elephant elephant--left" role="img" aria-label="Ausschnitt eines geschmückten Elefanten am linken Rand"></div>
    <div class="phone">
      <svg viewBox="0 0 24 32" aria-hidden="true">
        <path fill="#ffffff" d="M6 2c1.2-.6 2.2-.2 2.8.8l2.4 4.2c.6 1 .3 2-.6 2.6l-1.8 1.2c-.4.3-.5.8-.3 1.3 1.2 3 2.8 5.8 5 8.2.3.4.9.5 1.3.2l1.8-1.2c.9-.6 2-.4 2.6.5l2.6 4c.6 1 .4 2-.4 2.7l-1.8 1.4c-1.6 1.2-4 1.3-6 0C8.4 24 3.6 16.6 2.6 9.2 2.3 6.8 3.2 4.6 4.8 3Z"/>
      </svg>
      <span>+41 77 000 12 34</span>
    </div>
    <p class="email">E-mail : info@lumo-thara.ch</p>
    <div class="elephant elephant--right" role="img" aria-label="Ausschnitt eines geschmückten Elefanten am rechten Rand"></div>
    <p class="website">www.lumo-thara.ch</p>
  </section>
</main>
</body>
</html>
```